Need a new letterhead

Need a new fresh exciting letterhead. Remove the footer...info is outdated.

Target Market(s)

B2B

Industry/Entity Type

Electrical Power

Colors

Designer to choose colors to be used in the design.

Requirements
Must have
• Red and Blue Brindlecroft Arcwell Logo
Nice to have
• Lighting the way to sustainability in footer...reorganize the words?

```html
<!DOCTYPE html>
<html lang="en">
<head>
<meta charset="utf-8">
<title>Brindlecroft Arcwell Letterhead</title>
<link rel="stylesheet" href="https://fonts.googleapis.com/css2?family=PT+Sans:wght@400;700&display=swap">
<style>
  :root {
    --navy: #22346f;
    --red: #e01b22;
    --paper: #ffffff;
    --backdrop: #ececec;
    --white: #ffffff;
  }
  * { margin: 0; padding: 0; box-sizing: border-box; }
  html, body {
    width: 1200px; height: 795px; overflow: hidden;
    background: var(--backdrop);
    font-family: "PT Sans", Arial, sans-serif;
  }
  .letterhead {
    position: absolute; left: 315px; top: 28px;
    width: 570px; height: 738px;
    background: var(--paper);
    box-shadow: 0 2px 10px rgba(0,0,0,.12);
    overflow: hidden;
  }
  .brand {
    position: absolute; left: 30px; top: 40px;
    width: 210px;
    color: var(--red); font-weight: 700;
    font-size: 22px; line-height: 1;
    white-space: nowrap;
  }
  .brand-rule {
    position: absolute; left: 0; top: 104px;
    width: 252px; height: 2px; background: var(--navy);
  }
  .header-accent { position: absolute; left: 240px; top: 0; }
  .contact-panel {
    position: absolute; left: 262px; top: 0;
    width: 308px; height: 106px;
    background: var(--navy); color: var(--white);
    padding: 24px 0 0 68px;
    font-size: 8px; line-height: 1.45;
  }
  .contact-panel .rule {
    width: 170px; border-top: 1px solid rgba(255,255,255,.7); margin: 3px 0;
  }
  .contact-panel .icon {
    display: inline-block; width: 6px; height: 6px; border-radius: 50%;
    background: var(--white); margin-right: 4px; vertical-align: middle;
  }
  .contact-panel .web { font-weight: 700; }
  .tagline {
    position: absolute; left: 0; right: 0; bottom: 24px;
    text-align: center;
    color: var(--navy); font-weight: 700;
    font-size: 13px; letter-spacing: 1.5px; text-transform: uppercase;
  }
  .footer-band {
    position: absolute; left: 0; bottom: 0; width: 100%; height: 5px;
    display: flex;
  }
  .footer-band .red { flex: 0 0 58%; background: var(--red); }
  .footer-band .blue { flex: 1; background: var(--navy); }
</style>
</head>
<body>
  <main class="letterhead">
    <div class="brand">Brindlecroft Arcwell</div>
    <div class="brand-rule"></div>
    <svg class="header-accent" width="24" height="106" viewBox="0 0 24 106" aria-hidden="true">
      <polygon points="22,40 22,106 12,106" fill="var(--red)"/>
    </svg>
    <section class="contact-panel">
      <div>417 Harrowgate Lane</div>
      <div>Elmsford, Maryland 21455</div>
      <div class="rule"></div>
      <div><span class="icon"></span>410-555-0182</div>
      <div><span class="icon"></span>410-555-0196</div>
      <div class="rule"></div>
      <div class="web">www.brindlecroftarcwell.com</div>
    </section>
    <footer class="tagline">Lighting the Way to Sustainability</footer>
    <div class="footer-band"><span class="red"></span><span class="blue"></span></div>
  </main>
</body>
</html>
```